Professional modern business card design

A business card for my nutrition business, wanting a professional look, with info clearly visible. Open to using logo colours too.

Would like key info on the front -
logo
my name and qualifications
email
phone number

and just an enlarged logo again / image on the back.

```html
<!DOCTYPE html>
<html lang="en">
<head>
<meta charset="utf-8">
<title>Lumen Nutrition – Business Card</title>
<link rel="stylesheet" href="https://fonts.googleapis.com/css2?family=Open+Sans:wght@300;400;600;700;800&display=swap">
<style>
  :root {
    --navy: #06293d;
    --lime: #d2dd2c;
    --olive: #8a8a62;
    --white: #ffffff;
    --edge: #d4d4d4;
    --page: #ffffff;
  }
  html, body {
    margin: 0;
    padding: 0;
    width: 1172px;
    height: 1200px;
    overflow: hidden;
    background: var(--page);
    font-family: "Open Sans", Arial, sans-serif;
  }
  .sheet {
    position: relative;
    width: 1172px;
    height: 1200px;
  }
  .card {
    position: absolute;
    top: 472px;
    width: 455px;
    height: 260px;
  }
  .card svg {
    display: block;
    width: 100%;
    height: 100%;
  }
  .card--back { left: 69px; }
  .card--front { left: 639px; }
  .brand-text { font-family: "Open Sans", Arial, sans-serif; font-weight: 700; }
  .name { font-family: "Open Sans", Arial, sans-serif; font-weight: 800; }
  .detail { font-family: "Open Sans", Arial, sans-serif; font-weight: 300; }
</style>
</head>
<body>
<main class="sheet">

  <!-- Back side: enlarged brand name -->
  <section class="card card--back" aria-label="Card back">
    <svg viewBox="0 0 497 284" xmlns="http://www.w3.org/2000/svg">
      <rect width="497" height="284" fill="var(--navy)"/>
      <text class="brand-text" fill="var(--white)">
        <tspan x="118" y="147" font-size="58">Lumen</tspan>
        <tspan x="118" y="202" font-size="52">Nutrition</tspan>
      </text>
    </svg>
  </section>

  <!-- Front side: brand, name, contact -->
  <section class="card card--front" aria-label="Card front">
    <svg viewBox="0 0 497 284" xmlns="http://www.w3.org/2000/svg">
      <rect x="0.5" y="0.5" width="496" height="283" fill="var(--white)" stroke="var(--edge)"/>
      <path class="swoosh-lime" d="M1,246 Q170,40 422,1 L436,1 Q160,80 10,283 L1,283 Z" fill="var(--lime)"/>
      <path class="swoosh-olive" d="M10,283 Q160,80 436,1 L444,1 Q175,85 20,283 Z" fill="var(--olive)"/>
      <path class="panel" d="M18,281 Q175,86 434,1 L496,1 L496,281 Z" fill="var(--navy)"/>
      <line x1="15" y1="282" x2="496" y2="282" stroke="var(--white)" stroke-width="1"/>

      <text class="brand-text" fill="var(--navy)">
        <tspan x="42" y="55" font-size="22">Lumen</tspan>
        <tspan x="42" y="76" font-size="20">Nutrition</tspan>
      </text>

      <text class="name" x="464" y="150" font-size="36" fill="var(--white)" text-anchor="end">Your name</text>
      <line x1="199" y1="156.5" x2="496" y2="156.5" stroke="var(--white)" stroke-width="1"/>
      <text class="detail" x="464" y="183" font-size="23" fill="var(--white)" text-anchor="end">Your Qualifications</text>
      <text class="detail" x="464" y="223" font-size="20" fill="var(--white)" text-anchor="end">email@website.com</text>
      <text class="detail" x="464" y="250" font-size="20" fill="var(--white)" text-anchor="end">999 999 9999</text>
    </svg>
  </section>

</main>
</body>
</html>
```